Halvery Metal Recyclers - www.halveryrecyclers.com.au

I've just rebranded my business and thought what better way to continue with this than getting a website.
It is going to be fairly basic for now. I've attached quite a few images, feel free to use whichever you like.
And pages description is also attached in a .doc file.
Updates

Hi, this is my first time having a website. I am open to anything and trust the experience and ideas you can bring forward. I will look at extending the deadline so I can take my time to give feedback as needed! Thank you all.

Target Market(s)

Mining and industrial and commercial sectors

Coding

Coded - Design and coding required

Number of Pages Required

5+ page

Requirements
Must have
• Logo/Phone number at the top of every page. "Scrap Metal Specialists" tag line at the top of every page.
Nice to have
• Top Navigation.

```html
<!DOCTYPE html>
<html lang="en">
<head>
<meta charset="utf-8">
<title>Halvery Metal Recyclers</title>
<link href="https://fonts.googleapis.com/css2?family=Manrope:wght@300;400;500;600;700;800&display=swap" rel="stylesheet">
<style>
:root{
  --navy:#18396a;
  --grey:#888a8c;
  --light:#f3f3f3;
  --stage:#e9ecf1;
  --ink:#2b2f36;
  --white:#ffffff;
}
*{box-sizing:border-box;margin:0;padding:0}
html,body{width:1200px;height:3179px;overflow:hidden}
body{background:var(--stage);font-family:'Manrope',sans-serif;color:var(--ink);position:relative}
.site{position:absolute;left:183px;top:277px;width:832px;background:var(--white)}
section,header,footer{position:relative;width:832px}
.abs{position:absolute}
.brand{font-weight:800;color:var(--navy);line-height:1;letter-spacing:.3px}
.bracket{font-weight:300;color:var(--navy);font-size:25px}
.bracket b{font-weight:700}

/* nav */
.topbar{height:56px;background:var(--light)}
.topbar .brand{left:31px;top:14px;font-size:14px}
.topbar .tagline{left:31px;top:33px;font-size:7px;color:var(--grey);font-weight:600;letter-spacing:.5px}
.nav{left:265px;top:24px;display:flex;gap:26px;font-size:7.5px;color:var(--grey)}
.nav .on{color:var(--navy);font-weight:600}
.nav-sep{left:544px;top:14px;width:1px;height:28px;background:#d7d9dc}
.call{left:572px;top:18px;display:flex;gap:8px;align-items:center}
.call small{display:block;font-size:6px;color:var(--grey)}
.call strong{display:block;font-size:7.5px;color:var(--navy);font-weight:600}
.cta-btn{left:684px;top:0;width:148px;height:56px;background:var(--navy);color:var(--white);font-size:8px;font-weight:500;display:flex;align-items:center;justify-content:center;gap:8px}

/* hero */
.hero{height:522px;background:radial-gradient(ellipse at 50% 40%,#6e6f71,#3b3c3e 70%,#2a2b2c)}
.hero-frame{left:180px;top:169px;width:474px;height:134px;border:1.5px solid var(--navy)}
.hero .kicker{left:0;width:832px;top:218px;text-align:center;font-size:8px;letter-spacing:9px;color:#d5d6d8}
.hero h1{left:0;width:832px;top:236px;text-align:center;color:var(--white);font-weight:400;font-size:46px;line-height:1.1}
.hero h1 b{display:block;font-size:62px;font-weight:800;line-height:1}

/* intro */
.intro{height:208px;display:flex}
.intro-text{width:505px;background:var(--navy);color:var(--white);font-size:12.5px;line-height:24px;padding:56px 100px 0 112px}
.intro-stat{width:165px;background:var(--light);text-align:center;padding-top:60px}
.intro-stat .num{font-size:58px;font-weight:200;color:#c9cbcf;line-height:1}
.intro-stat p{font-size:10.5px;color:var(--navy);margin-top:4px}
.intro-photo{width:162px;background:linear-gradient(135deg,#9a9b9d,#4e4f51)}

/* services */
.services{height:305px}
.services h2{left:111px;top:60px}
.services .lede{left:111px;top:106px;width:240px;font-size:8px;line-height:16px;color:var(--grey)}
.svc{width:150px;font-size:7.5px;color:var(--navy);font-weight:500}
.svc svg{display:block;margin-bottom:14px}

/* about */
.about{height:387px}
.about-bg{left:198px;top:0;width:634px;height:387px;background:linear-gradient(120deg,#f1f1f2,#e8e9eb)}
.about-block{left:201px;top:192px;width:110px;height:155px;background:var(--navy)}
.about-photo{left:117px;top:62px;width:172px;height:264px;background:linear-gradient(160deg,#b7b8ba,#6a6b6d)}
.about h2{left:443px;top:102px}
.about .copy{left:443px;top:154px;width:285px;font-size:8px;line-height:16.5px;color:#5d6168}
.about .copy p+p{margin-top:9px}
.about .arrow{left:443px;top:300px}

/* quote */
.quote{height:523px}
.quote h2{left:0;width:832px;top:64px;text-align:center}
.side-bar{top:140px;width:10px;height:242px;background:var(--navy)}
.form{left:167px;top:122px;width:500px}
.row{display:flex;gap:10px;margin-bottom:21px}
.field{flex:1}
.field label{display:block;font-size:6px;color:var(--grey);margin:0 0 6px 3px}
.field .box{height:30px;border:1px solid #e1e2e4;background:#fafafa}
.field .box.tall{height:114px}
.submit{left:0;width:832px;top:454px;text-align:center;font-size:8px;color:var(--navy);font-weight:600}

/* news */
.news{height:460px}
.news-bg{left:0;top:0;width:585px;height:460px;background:var(--light)}
.news h2{left:114px;top:65px}
.post{left:115px;display:flex;gap:10px}
.thumb{width:62px;height:62px;background:linear-gradient(135deg,#a3a4a6,#55565a)}
.meta{padding-top:8px}
.date{font-size:6.5px;color:var(--grey);letter-spacing:.5px}
.title{font-size:12px;color:var(--ink);margin:4px 0 3px}
.read{font-size:6px;color:var(--grey)}
.feature{left:435px;top:134px}
.feature .img{width:285px;height:166px;background:linear-gradient(150deg,#c5c6c8,#6d6e70)}
.feature .meta{padding-top:20px}

/* footer */
.footer{height:329px;background:var(--navy);color:var(--white)}
.footer h3{left:107px;top:70px;font-size:22px;font-weight:500;line-height:30px}
.footer h3 span{color:#8f9fbb}
.tick{left:706px;top:82px}
.footer .rule{left:107px;top:147px;width:618px;height:1px;background:#2f4e7d}
.f-brand{left:111px;top:186px}
.f-brand .brand{color:var(--white);font-size:15px}
.f-brand .since{font-size:15px;color:#8f9fbb;margin-top:6px;font-weight:500}
.f-brand small{display:block;font-size:6px;margin-top:8px}
.col h4{font-size:10.5px;font-weight:600;margin-bottom:9px}
.col p,.col li{font-size:6.5px;color:#c4cddc;list-style:none;line-height:16px}
.socials{display:flex;gap:8px}
.socials i{width:20px;height:20px;border-radius:50%;background:var(--white);display:block}
</style>
</head>
<body>
<main class="site">

  <header class="topbar">
    <div class="abs brand">HALVERY</div>
    <div class="abs tagline">SCRAP METAL SPECIALISTS</div>
    <nav class="abs nav"><span class="on">Home</span><span>About</span><span>Services</span><span>Online Store</span><span>Blog</span></nav>
    <div class="abs nav-sep"></div>
    <div class="abs call">
      <svg width="20" height="20" viewBox="0 0 24 24" fill="none" stroke="#18396a" stroke-width="1.4"><path d="M5 3h4l2 5-3 2a12 12 0 0 0 6 6l2-3 5 2v4a2 2 0 0 1-2 2A18 18 0 0 1 3 5a2 2 0 0 1 2-2z"/></svg>
      <div><small>Call Us Anytime</small><strong>0412555018</strong></div>
    </div>
    <a class="abs cta-btn">Make An Inquiry <svg width="18" height="6" viewBox="0 0 18 6"><path d="M0 3h16M13 .5 17 3l-4 2.5" stroke="#fff" fill="none"/></svg></a>
  </header>

  <section class="hero" role="img" aria-label="Black and white photo of large geared scrap metal rings in a yard">
    <div class="abs hero-frame"></div>
    <p class="abs kicker">WELCOME TO OUR WEBSITE</p>
    <h1 class="abs">Halvery Metal<b>Recyclers</b></h1>
  </section>

  <section class="intro">
    <div class="intro-text">We are a Perth based company that provides scrap metal collection &amp; oxy cutting services in the mining, construction, and industrial sectors all around WA.</div>
    <div class="intro-stat"><div class="num">16+</div><p>Years of Experiece</p></div>
    <div class="intro-photo" role="img" aria-label="Photo of scrap metal pipes"></div>
  </section>

  <section class="services">
    <h2 class="abs bracket">[ Our <b>Services</b></h2>
    <p class="abs lede">We appreciate your trust. Our clients choose us and our products because they know we're the best.</p>
    <div class="abs svc" style="left:449px;top:62px"><svg width="44" height="44" viewBox="0 0 44 44" fill="none" stroke="#888a8c" stroke-width="1.3"><rect x="16" y="22" width="20" height="12"/><path d="M6 30 10 6l12 10"/><rect x="14" y="34" width="24" height="6" rx="3"/></svg>LARGE MINING MACHINERY</div>
    <div class="abs svc" style="left:597px;top:62px"><svg width="50" height="44" viewBox="0 0 50 44" fill="none" stroke="#888a8c" stroke-width="1.3"><rect x="4" y="8" width="20" height="18"/><path d="M28 18h14M38 14l4 4-4 4"/><rect x="2" y="30" width="46" height="8" rx="4"/></svg>LARGE MINESITE INFRASTRUCTURE</div>
    <div class="abs svc" style="left:111px;top:180px"><svg width="44" height="44" viewBox="0 0 44 44" fill="none" stroke="#888a8c" stroke-width="1.3"><circle cx="22" cy="7" r="3"/><path d="M22 10v28M14 16h16M6 26a16 14 0 0 0 32 0"/></svg>SUBSEA</div>
    <div class="abs svc" style="left:253px;top:180px"><svg width="44" height="44" viewBox="0 0 44 44" fill="none" stroke="#888a8c" stroke-width="1.3"><path d="M6 20h32l-4 14H10z"/><circle cx="14" cy="38" r="3"/><circle cx="30" cy="38" r="3"/><path d="M12 20l4-8h12l4 8"/></svg>HEAVY INDUSTRIAL EQUIPMENT</div>
    <div class="abs svc" style="left:449px;top:180px"><svg width="44" height="44" viewBox="0 0 44 44" fill="none" stroke="#888a8c" stroke-width="1.3"><path d="M14 2v40M30 2v40M14 8h16M14 16h16M14 24h16M14 32h16M14 40h16"/></svg>RAIL</div>
    <div class="abs svc" style="left:597px;top:180px"><svg width="44" height="44" viewBox="0 0 44 44" fill="none" stroke="#888a8c" stroke-width="1.3"><path d="M10 30a12 12 0 1 1 24 0"/><path d="M22 8v22M16 22l6 8 6-8"/><path d="M6 38h32"/></svg>MINESITE CLEAN UPS &amp; DEMOLITION</div>
  </section>

  <section class="about">
    <div class="abs about-bg"></div>
    <div class="abs about-block"></div>
    <div class="abs about-photo" role="img" aria-label="Photo of a smiling worker in hard hat and overalls in a scrap yard"></div>
    <h2 class="abs bracket">[ About <b>HMR</b></h2>
    <div class="abs copy">
      <p>My name is Tom Halvery and I'm the managing director of Halvery Metal Processors. I have been in the scrap metal recycling industry longer than I haven't! I have <b>16 years' experience</b> in everything scrap metal and I am very passionate about sustainable recycling.</p>
      <p>Lorem Ipsum is simply dummy text of the printing and typesetting industry. Lorem Ipsum has been the industry's standard dummy text ever since the 1500s and some more text filler.</p>
    </div>
    <svg class="abs arrow" width="18" height="6" viewBox="0 0 18 6"><path d="M0 3h16M13 .5 17 3l-4 2.5" stroke="#18396a" fill="none"/></svg>
  </section>

  <section class="quote">
    <h2 class="abs bracket">[ Request a <b>Quote</b></h2>
    <div class="abs side-bar" style="left:0"></div>
    <div class="abs side-bar" style="left:822px"></div>
    <div class="abs form">
      <div class="row"><div class="field"><label>First Name*</label><div class="box"></div></div><div class="field"><label>Last Name*</label><div class="box"></div></div></div>
      <div class="row"><div class="field"><label>Email Address*</label><div class="box"></div></div><div class="field"><label>Phone Number*</label><div class="box"></div></div><div class="field"><label>City*</label><div class="box"></div></div></div>
      <div class="row"><div class="field"><label>Zip*</label><div class="box"></div></div><div class="field"><label>Type of Service*</label><div class="box"></div></div></div>
      <div class="row"><div class="field"><label>Comments*</label><div class="box tall"></div></div></div>
    </div>
    <p class="abs submit">Submit Request &nbsp;<svg width="18" height="6" viewBox="0 0 18 6"><path d="M0 3h16M13 .5 17 3l-4 2.5" stroke="#18396a" fill="none"/></svg></p>
  </section>

  <section class="news">
    <div class="abs news-bg"></div>
    <h2 class="abs bracket">[ Company <b>News</b></h2>
    <article class="abs post" style="top:134px"><div class="thumb" role="img" aria-label="Photo of scrap metal"></div><div class="meta"><div class="date">11/18/2022</div><div class="title">What is the price scrapping?</div><div class="read">+ READ STORY</div></div></article>
    <article class="abs post" style="top:222px"><div class="thumb" role="img" aria-label="Photo of metal cutting"></div><div class="meta"><div class="date">11/18/2022</div><div class="title">Is scrapping worth it?</div><div class="read">+ READ STORY</div></div></article>
    <article class="abs post" style="top:310px"><div class="thumb" role="img" aria-label="Photo of an excavator bucket"></div><div class="meta"><div class="date">11/18/2022</div><div class="title">Why scrapping is taking over?</div><div class="read">+ READ STORY</div></div></article>
    <article class="abs feature"><div class="img" role="img" aria-label="Photo of a worker beside heavy machinery"></div><div class="meta"><div class="date">11/18/2022</div><div class="title">Full time scrapping: Is it an option for you?</div><div class="read">+ READ STORY</div></div></article>
  </section>

  <footer class="footer">
    <h3 class="abs">Let's work together! We are here to<br><span>help you</span> and answer your questions</h3>
    <svg class="abs tick" width="16" height="16" viewBox="0 0 16 16"><path d="M2 14 14 2M9 2h5v5" stroke="#fff" fill="none" stroke-width="1.2"/></svg>
    <div class="abs rule"></div>
    <div class="abs f-brand"><div class="brand">HALVERY</div><div class="since">since 2008</div><small>© 2022 HMR</small></div>
    <div class="abs col" style="left:280px;top:176px"><h4>Location</h4><p>Some Dummy Text Filler Goes Here</p></div>
    <div class="abs col" style="left:280px;top:234px"><h4>Social Media</h4><div class="socials"><i></i><i></i></div></div>
    <div class="abs col" style="left:473px;top:176px"><h4>Phone</h4><p>0412555018</p></div>
    <div class="abs col" style="left:473px;top:232px"><h4>Email</h4><p>tom@halveryrecyclers.com.au</p></div>
    <div class="abs col" style="left:657px;top:176px"><h4>Quick Links</h4><ul><li>Home</li><li>Services</li><li>Contact</li><li>Shop</li></ul></div>
  </footer>

</main>
</body>
</html>
```